Tradewell Banner Design for B2B Consulting Firm

Take the already developed logo (attached) and incorporate it into a creative banner design for placement on Tradewell (the social media platform targeting business users). The banner will be used on the firm's company profile page on Tradewell (not yet created).

```html
<!DOCTYPE html>
<html lang="en">
<head>
<meta charset="utf-8">
<title>Corvane Partners – Tradewell Banners</title>
<link rel="stylesheet" href="https://fonts.googleapis.com/css2?family=Questrial&family=Lora:wght@400;500&display=swap">
<style>
  :root {
    --page: #c8c6c7;
    --green: #47654c;
    --green-deep: #0f3a1f;
    --green-bright: #1f8a45;
    --light: #f4f4f4;
  }
  html, body {
    margin: 0;
    padding: 0;
    width: 1200px;
    height: 686px;
    overflow: hidden;
    background: var(--page);
  }
  .banner-set {
    display: block;
    width: 1200px;
    height: 686px;
  }
  .fill-green { fill: var(--green); }
  .fill-light { fill: var(--light); }
  .stroke-light { fill: none; stroke: var(--light); }
  .sans { font-family: "Questrial", "Century Gothic", sans-serif; }
  .serif { font-family: "Lora", Georgia, serif; }
  .tagline { font-size: 51.5px; }
  .tagline-serif { font-size: 50px; }
  .brand-name { font-size: 56px; }
  .contact { font-size: 19.5px; }
  .contact-serif { font-size: 20px; }
  .on-green { fill: var(--light); }
  .on-light { fill: var(--green); }
</style>
</head>
<body>
<svg class="banner-set" viewBox="0 0 2550 1456" preserveAspectRatio="none" xmlns="http://www.w3.org/2000/svg">
  <defs>
    <symbol id="icon-phone" viewBox="0 0 20 20">
      <path d="M4 3 L8 3 L9 7 L7 8.5 C8.2 11 9.5 12.3 12 13.5 L13.5 11.5 L17 12.5 L17 16.5 C10 17.5 2.5 10 4 3 Z" fill="currentColor"/>
    </symbol>
    <symbol id="icon-pin" viewBox="0 0 20 20">
      <path d="M10 1.5 C6.4 1.5 4 4.2 4 7.5 C4 11.5 10 18.5 10 18.5 C10 18.5 16 11.5 16 7.5 C16 4.2 13.6 1.5 10 1.5 Z M10 5 A2.6 2.6 0 1 1 9.99 5 Z" fill="currentColor" fill-rule="evenodd"/>
    </symbol>
    <symbol id="icon-globe" viewBox="0 0 20 20">
      <g fill="none" stroke="currentColor" stroke-width="1.2">
        <circle cx="10" cy="10" r="8.5"/>
        <ellipse cx="10" cy="10" rx="3.8" ry="8.5"/>
        <line x1="1.5" y1="10" x2="18.5" y2="10"/>
        <path d="M3 5.5 H17 M3 14.5 H17"/>
      </g>
    </symbol>
    <symbol id="icon-chevrons" viewBox="0 0 60 50">
      <g fill="none" stroke="currentColor" stroke-width="4.5" stroke-linejoin="miter">
        <polyline points="3,3 21,25 3,47"/>
        <polyline points="19,3 37,25 19,47"/>
        <polyline points="35,3 53,25 35,47"/>
      </g>
    </symbol>

    <clipPath id="clip-banner-top"><rect x="61" y="70" width="2430" height="412"/></clipPath>
    <clipPath id="clip-banner-middle-panel"><polygon points="61,537 885,537 1030,732 885,928 61,928"/></clipPath>
    <clipPath id="clip-banner-bottom"><rect x="61" y="975" width="2430" height="412"/></clipPath>

    <linearGradient id="photo-tones" x1="0" y1="0" x2="1" y2="0.35">
      <stop offset="0" stop-color="#0c2a16"/>
      <stop offset="0.3" stop-color="#1d6b37"/>
      <stop offset="0.55" stop-color="#5d8f6a"/>
      <stop offset="0.75" stop-color="#1f8a45"/>
      <stop offset="1" stop-color="#0f4a24"/>
    </linearGradient>
  </defs>

  <g class="banner banner--green">
    <rect class="fill-green" x="61" y="70" width="2430" height="412"/>
    <circle class="fill-light" cx="224" cy="415" r="128" clip-path="url(#clip-banner-top)"/>

    <text class="sans tagline on-green" x="373" y="262">The best corporate</text>
    <text class="sans tagline on-green" x="373" y="319">marketing services</text>

    <g class="brand">
      <rect class="fill-light" x="1256" y="170" width="40" height="40"/>
      <text class="sans brand-name on-green" x="1276" y="330" text-anchor="middle">Corvane Partners</text>
    </g>

    <text class="sans tagline on-green" x="1783" y="262">Fractional Marketing</text>
    <text class="sans tagline on-green" x="1783" y="319">&amp; Business Development</text>

    <g class="contact-row" style="color: var(--light)">
      <use href="#icon-phone" x="842" y="418" width="20" height="20"/>
      <text class="sans contact on-green" x="872" y="434">(555) 210-xxxx</text>
      <use href="#icon-pin" x="1013" y="418" width="20" height="20"/>
      <text class="sans contact on-green" x="1042" y="434">48 Maple Lane, Unit 210 . Brookfield, CT 06000 . USA</text>
      <use href="#icon-globe" x="1525" y="418" width="20" height="20"/>
      <text class="sans contact on-green" x="1558" y="434">corvanepartners.com</text>
    </g>
  </g>

  <g class="banner banner--chevron">
    <rect class="fill-light" x="61" y="517" width="2430" height="430"/>
    <polygon class="fill-green" points="61,537 885,537 1030,732 885,928 61,928"/>
    <circle class="fill-light" cx="224" cy="870" r="128" clip-path="url(#clip-banner-middle-panel)"/>

    <polygon class="fill-green" points="897,517 1655,517 1812,732 1655,947 897,947 1057,732"/>
    <polygon class="fill-light" points="955,537 1578,537 1722,732 1578,928 955,928 1110,732"/>
    <polyline class="stroke-light" stroke-width="22" points="1612,530 1760,732 1612,934"/>

    <polygon role="img" aria-label="Photo of a business handshake in green tones" fill="url(#photo-tones)"
             points="1705,527 2491,527 2491,937 1705,937 1860,732"/>

    <g class="contact-list" style="color: var(--light)">
      <use href="#icon-pin" x="112" y="577" width="20" height="20"/>
      <text class="sans contact on-green" x="142" y="593">48 Maple Lane, Unit 210 . Brookfield, CT 06000 . USA</text>
      <use href="#icon-phone" x="114" y="619" width="20" height="20"/>
      <text class="sans contact on-green" x="145" y="635">(555) 210-xxxx</text>
      <use href="#icon-globe" x="115" y="662" width="20" height="20"/>
      <text class="sans contact on-green" x="149" y="678">corvanepartners.com</text>
      <use href="#icon-chevrons" x="733" y="570" width="60" height="50"/>
    </g>

    <text class="sans tagline on-green" x="475" y="720">The best corporate</text>
    <text class="sans tagline on-green" x="475" y="777">marketing services</text>

    <g class="brand">
      <rect class="fill-green" x="1351" y="650" width="40" height="40"/>
      <text class="sans brand-name on-light" x="1371" y="808" text-anchor="middle">Corvane Partners</text>
    </g>

    <use href="#icon-chevrons" x="1842" y="856" width="60" height="50" style="color: var(--light)"/>
  </g>

  <g class="banner banner--light">
    <rect class="fill-light" x="61" y="975" width="2430" height="412"/>
    <circle class="fill-green" cx="224" cy="1320" r="128" clip-path="url(#clip-banner-bottom)"/>

    <polygon role="img" aria-label="Photo of a business handshake in green tones" fill="url(#photo-tones)"
             points="1730,975 2491,975 2491,1387 1730,1387 1597,1180"/>

    <g class="contact-row" style="color: var(--green)">
      <use href="#icon-phone" x="114" y="1030" width="20" height="20"/>
      <text class="serif contact-serif on-light" x="144" y="1047">(555) 210-xxxx</text>
      <use href="#icon-pin" x="289" y="1029" width="20" height="20"/>
      <text class="serif contact-serif on-light" x="318" y="1045">48 Maple Lane, Unit 210 . Brookfield, CT 06000 . USA</text>
      <use href="#icon-globe" x="836" y="1029" width="20" height="20"/>
      <text class="serif contact-serif on-light" x="870" y="1045">corvanepartners.com</text>
    </g>

    <text class="serif tagline-serif on-light" x="473" y="1193">The best corporate</text>
    <text class="serif tagline-serif on-light" x="473" y="1257">marketing services</text>

    <g class="brand">
      <rect class="fill-green" x="1256" y="1090" width="40" height="40"/>
      <text class="sans brand-name on-light" x="1276" y="1250" text-anchor="middle">Corvane Partners</text>
    </g>
  </g>
</svg>
</body>
</html>
```